依頼詳細
どちらかと言えば、可愛いより、カッコイイ感じの名刺をお願いします。
横向きでお願いします。
背景は、両面共、白より、黒やグレー、シルバーなどシックな感じの色希望です。
ロゴはそれにあった色を希望します。
その他、デザイナー様でおすすめの色などありましたら、お任せします。
記載項目
表面:会社名/役職/名前/ローマ字読み仮名/住所/電話/FAX/mail
裏面:事業内容
表面には必ず指定ロゴをいれてください。
希望イメージ
シンプル 複雑
単色 カラフル
暗い 明るい
日常 高級
遊び心 厳粛
未来的 伝統的
女性的 男性的
希望する色
茶系、グレー系
納品ファイル
• 高解像度JPG (.jpg)
• イラストレーター形式 (.ai)
補足説明
■ 選んだ理由

第一印象が良かった事と、ロゴの特徴が生かせていて特別感を感じた所です。

■ 提案者全員のお礼・コメント

たくさんのご応募ありがとうございました。

```html
<!DOCTYPE html>
<html lang="ja">
<head>
<meta charset="utf-8">
<title>Nova 8 名刺デザイン</title>
<link rel="stylesheet" href="https://fonts.googleapis.com/css2?family=Noto+Sans+JP:wght@400;500&display=swap">
<style>
  :root{
    --sheet:#e6e6e6;
    --label:#333333;
    --card-white:#ffffff;
    --ink:#1e1a18;
    --band:#2a2421;
    --on-band:#ffffff;
    --grey-light:#d9d9d9;
    --grey-mid:#9b9b9b;
    --grey-dark:#4a4a4a;
  }
  *{box-sizing:border-box;margin:0;padding:0}
  html,body{width:800px;height:1200px;overflow:hidden;background:var(--sheet)}
  body{position:relative;font-family:"Noto Sans JP",sans-serif;color:var(--ink)}
  .side-label{position:absolute;left:40px;font-size:18px;color:var(--label);font-weight:400}
  .side-label.front{top:72px}
  .side-label.back{top:618px}
  .card{position:absolute;left:40px;width:720px;height:436px;overflow:hidden;box-shadow:0 1px 3px rgba(0,0,0,.25)}
  .card.front{top:120px;background:var(--card-white)}
  .card.back{top:667px}
  .card svg.card-art{position:absolute;inset:0;width:720px;height:436px}

  .person{position:absolute;left:62px;top:64px}
  .person .role{font-size:14px;letter-spacing:1px}
  .person .name{margin-top:6px;font-size:34px;letter-spacing:6px;font-weight:500;line-height:1.1}
  .person .name .roman{font-size:13px;letter-spacing:0;margin-left:10px;vertical-align:middle;font-weight:400}
  .person .mobile{margin-top:6px;font-size:16px;display:flex;align-items:center;gap:6px}
  .icon-phone{width:10px;height:16px;border:2px solid var(--ink);border-radius:2px}

  .brand{position:absolute;color:var(--card-white);font-weight:400;letter-spacing:1px}
  .front .brand{right:40px;top:194px;font-size:38px;color:var(--grey-dark)}
  .back .brand{left:62px;top:76px;font-size:42px}

  .contact{position:absolute;left:40px;top:318px;color:var(--on-band);font-size:15px;line-height:30px}
  .contact li{list-style:none;display:flex;align-items:center;gap:8px}
  .contact .ico{width:14px;height:12px;background:var(--on-band);border-radius:2px;flex:none}
  .contact .sep{margin-left:10px}

  .services{position:absolute;left:356px;top:180px;color:var(--card-white)}
  .services h2{font-size:13px;font-weight:500;margin-bottom:6px}
  .services p{font-size:12.5px;letter-spacing:0.5px;line-height:25px}
</style>
</head>
<body>
  <div class="side-label front">Front</div>
  <section class="card front">
    <svg class="card-art" viewBox="0 0 720 436" aria-hidden="true">
      <defs>
        <linearGradient id="sweepDark" x1="0" y1="1" x2="1" y2="0">
          <stop offset="0" stop-color="#e0e0e0"/>
          <stop offset=".5" stop-color="#8a8a8a"/>
          <stop offset="1" stop-color="#3e3e3e"/>
        </linearGradient>
        <linearGradient id="sweepLight" x1="0" y1="1" x2="1" y2="0">
          <stop offset="0" stop-color="#ffffff"/>
          <stop offset="1" stop-color="#c8c8c8"/>
        </linearGradient>
      </defs>
      <path d="M0,200 C230,235 460,150 720,20 L720,70 C450,200 220,262 0,240 Z" fill="url(#sweepLight)"/>
      <path d="M0,236 C230,262 470,180 720,60 L720,150 C470,250 240,282 0,278 Z" fill="url(#sweepDark)"/>
      <path d="M120,262 C330,260 520,190 720,100" stroke="#ffffff" stroke-width="2" fill="none" opacity=".8"/>
      <rect x="0" y="277" width="720" height="159" fill="var(--band)"/>
    </svg>
    <div class="person">
      <div class="role">代表取締役</div>
      <div class="name">佐藤 健<span class="roman">Ken Sato</span></div>
      <div class="mobile"><span class="icon-phone"></span>Mobile : 080-2468-1357</div>
    </div>
    <div class="brand">Nova 8</div>
    <ul class="contact">
      <li><span class="ico"></span>650-0091 架空県青葉市緑町5-6-7 中央ビル 3F</li>
      <li><span class="ico"></span>Tel : 078-555-0142<span class="ico sep"></span>Fax : 078-555-0143</li>
      <li><span class="ico"></span>contact@nova8.example</li>
    </ul>
  </section>

  <div class="side-label back">Back</div>
  <section class="card back">
    <svg class="card-art" viewBox="0 0 720 436" aria-hidden="true">
      <defs>
        <linearGradient id="backBase" x1="0" y1="0" x2="1" y2="0">
          <stop offset="0" stop-color="#8c8c8c"/>
          <stop offset=".55" stop-color="#6a6a6a"/>
          <stop offset="1" stop-color="#2e2e2e"/>
        </linearGradient>
        <linearGradient id="backWave" x1="0" y1="0" x2="1" y2="1">
          <stop offset="0" stop-color="#f2f2f2"/>
          <stop offset="1" stop-color="#8e8e8e"/>
        </linearGradient>
      </defs>
      <rect width="720" height="436" fill="url(#backBase)"/>
      <path d="M0,0 L560,0 C420,70 240,200 0,300 Z" fill="url(#backWave)" opacity=".9"/>
      <path d="M0,300 C240,200 420,70 560,0" stroke="#ffffff" stroke-width="2" fill="none" opacity=".7"/>
      <rect x="0" y="398" width="720" height="38" fill="var(--band)"/>
    </svg>
    <div class="brand">Nova 8</div>
    <div class="services">
      <h2>【業務内容】</h2>
      <p>□□□□□□□□□□□□□□□□□□□□□□</p>
      <p>□□□□□□□□□□□□□□□□□□□□□□</p>
      <p>□□□□□□□□□□□□□□□□□□□□□□</p>
      <p>□□□□□□□□□□□□□□□□□□□□□□</p>
      <p>□□□□□□□□□□□□□□□□□□□□□□</p>
    </div>
  </section>
</body>
</html>
```